a promotional poster design to promote our upcoming event. We want the date to be promoted as "Save the Date" for Sunday 4th July 2021.

Requirements
Must have
• the following text;

Save the Date! (stand out)
Sunday 4th July 2021 (stand out)
KTRB Family Mixed Netball Carnival
Nice to have
• make the date stand out. We want people to lock in the date we're promoting.

```html
<!DOCTYPE html>
<html lang="en">
<head>
<meta charset="utf-8">
<title>Save the Date – KTRB Family Mixed Netball Carnival</title>
<link href="https://fonts.googleapis.com/css2?family=Anton&display=swap" rel="stylesheet">
<style>
  :root {
    --ink: #181818;
    --gold-dark: #a8862a;
    --gold: #d9b94c;
    --gold-light: #f0dc86;
    --silver-dark: #9a9a9a;
    --silver: #d6d6d6;
    --silver-light: #f4f4f4;
    --white: #ffffff;
    --red: #e41e26;
    --yellow: #ffd400;
  }
  html, body {
    margin: 0;
    padding: 0;
    width: 886px;
    height: 1200px;
    overflow: hidden;
    background: var(--ink);
  }
  .poster {
    position: relative;
    width: 886px;
    height: 1200px;
    background: var(--ink);
    font-family: "Anton", "Arial Narrow", sans-serif;
    text-transform: uppercase;
    overflow: hidden;
  }
  .poster__frame {
    position: absolute;
    inset: 3px;
    border: 2px solid var(--gold);
    pointer-events: none;
  }
  .gold-text {
    background: linear-gradient(180deg, var(--gold-light) 0%, var(--gold) 45%, var(--gold-dark) 100%);
    -webkit-background-clip: text;
    background-clip: text;
    color: transparent;
  }
  .silver-text {
    background: linear-gradient(180deg, var(--silver-light) 0%, var(--silver) 50%, var(--silver-dark) 100%);
    -webkit-background-clip: text;
    background-clip: text;
    color: transparent;
  }
  .org {
    position: absolute;
    top: 72px;
    left: 0;
    width: 100%;
    text-align: center;
    color: var(--white);
  }
  .org__mark {
    display: block;
    width: 40px;
    height: 40px;
    margin: 0 auto 48px;
    background: var(--red);
  }
  .org__name {
    font-size: 20px;
    line-height: 1.1;
    letter-spacing: 0.5px;
  }
  .headline-top {
    position: absolute;
    top: 244px;
    left: 0;
    width: 100%;
    margin: 0;
    text-align: center;
    font-size: 122px;
    font-weight: 400;
    line-height: 1;
    letter-spacing: 0;
  }
  .headline-main {
    position: absolute;
    top: 368px;
    left: 121px;
    display: flex;
    align-items: flex-end;
    gap: 22px;
    font-size: 232px;
    line-height: 1;
  }
  .headline-main__word {
    letter-spacing: 36px;
  }
  .headline-main__bang {
    font-size: 236px;
  }
  .event-date {
    position: absolute;
    top: 630px;
    left: 0;
    width: 100%;
    display: flex;
    justify-content: center;
    align-items: center;
    gap: 34px;
  }
  .event-date__rule {
    width: 57px;
    height: 3px;
    background: var(--gold);
  }
  .event-date__text {
    font-size: 62px;
    line-height: 1;
    letter-spacing: 3px;
    word-spacing: 12px;
  }
  .campaign-artwork {
    position: absolute;
    top: 725px;
    left: 161px;
    width: 530px;
    height: 378px;
    border-radius: 60px;
    background: radial-gradient(ellipse at 45% 45%, var(--yellow) 0%, var(--red) 55%, var(--ink) 100%);
  }
  .event-name {
    position: absolute;
    top: 1120px;
    left: 0;
    width: 100%;
    margin: 0;
    text-align: center;
    font-size: 47px;
    line-height: 1;
    letter-spacing: 3.5px;
    word-spacing: 4px;
  }
</style>
</head>
<body>
  <main class="poster">
    <div class="poster__frame"></div>

    <header class="org">
      <span class="org__mark"></span>
      <div class="org__name">KTRB Community<br>Health</div>
    </header>

    <h1 class="headline-top gold-text">Save the</h1>
    <div class="headline-main">
      <span class="headline-main__word gold-text">Date</span>
      <span class="headline-main__bang silver-text">!</span>
    </div>

    <div class="event-date">
      <span class="event-date__rule"></span>
      <span class="event-date__text"><span class="silver-text">Sunday</span> <span class="gold-text">4th July</span> <span class="silver-text">2021</span></span>
      <span class="event-date__rule"></span>
    </div>

    <div class="campaign-artwork" role="img" aria-label="Hand-lettered anti-smoking campaign slogan in bold red and yellow brush lettering"></div>

    <p class="event-name gold-text">KTRB Family Mixed Netball Carnival</p>
  </main>
</body>
</html>
```